mediation practice website build

Looking to create a website for new civil mediation practice. Pages would be "home", "about us", "about mediation", "scheduling" (perhaps with some kind of calendar function), "contact us". Would love to be able to update content/text myself.
Target Market(s)
Small to midsize businesses and attorneys representing those size businesses in pending disputes.
Industry/Entity Type
Build
Look and feel
Each slider illustrates characteristics of the customer's brand and the style your logo design should communicate.

```html
<!DOCTYPE html>
<html lang="en">
<head>
<meta charset="utf-8">
<title>Harbourline Mediation – Home</title>
<link rel="stylesheet" href="https://fonts.googleapis.com/css2?family=Noto+Sans:wght@400;700&family=Orbitron:wght@500&display=swap">
<style>
  :root {
    --slate: #4a5878;
    --navy: #000066;
    --ink: #1d2a1d;
    --logo-blue: #1b4a8c;
    --sky: #c6d7f6;
    --panel: #fbfbfb;
    --bullet: #2b3a2b;
    --white: #ffffff;
  }
  * { margin: 0; padding: 0; box-sizing: border-box; }
  html, body { width: 1200px; height: 885px; overflow: hidden; background: var(--white); }
  body { position: relative; font-family: "Noto Sans", Verdana, sans-serif; color: var(--ink); }

  .frame { position: absolute; inset: 0; }

  .site-header {
    position: absolute; left: 248px; top: 12px; width: 865px; height: 210px;
    background: var(--white);
  }
  .banner {
    position: absolute; left: 0; top: 0; width: 865px; height: 130px;
    background: linear-gradient(90deg, var(--white) 0%, #e4ecfb 35%, var(--sky) 75%, #b8c9ea 100%);
  }
  .banner-photo {
    position: absolute; right: 0; top: 0; width: 373px; height: 130px;
    background: radial-gradient(ellipse 150px 60px at 56% 55%, var(--slate) 0 98%, transparent 100%),
                linear-gradient(120deg, #dfe7f6 0%, #8f9fbd 50%, #52607f 100%);
  }
  .brand {
    position: absolute; left: 20px; top: 36px; width: 252px; height: 79px;
    background: var(--white);
    display: flex; flex-direction: column; justify-content: center; padding-left: 6px;
    font-family: "Noto Sans", Verdana, sans-serif; font-weight: 700;
    font-size: 29px; line-height: 32px; letter-spacing: 1px; color: var(--logo-blue);
    text-transform: uppercase;
  }

  .main-nav a {
    position: absolute; height: 40px;
    background: var(--navy); color: var(--white); text-decoration: none;
    font-family: "Orbitron", "Arial Narrow", sans-serif; font-weight: 500;
    font-size: 13px; letter-spacing: 1px; text-transform: uppercase;
    display: flex; align-items: center; justify-content: center; padding-bottom: 6px;
  }
  .nav-home { left: 11px; top: 135px; width: 101px; }
  .nav-about { left: 140px; top: 136px; width: 150px; }
  .nav-mediation { left: 321px; top: 138px; width: 200px; }
  .nav-scheduling { left: 547px; top: 137px; width: 150px; }
  .nav-contact { left: 718px; top: 137px; width: 149px; }

  .header-rule { position: absolute; left: 248px; top: 222px; width: 867px; height: 3px; background: #7a86a0; }

  .content {
    position: absolute; left: 248px; top: 258px; width: 582px; height: 376px;
    background: var(--panel); padding: 0 3px;
    font-size: 11.5px; line-height: 12px;
  }
  .content h2 { font-size: 11.5px; line-height: 12px; font-weight: 700; }
  .content p { margin-bottom: 12px; }
  .gap { height: 36px; }

  .services { position: absolute; top: 696px; font-size: 12px; font-weight: 700; display: flex; align-items: center; gap: 6px; }
  .services::before { content: ""; width: 14px; height: 14px; border-radius: 50%; background: var(--bullet); }
  .svc-one { left: 255px; }
  .svc-two { left: 621px; top: 694px; }
</style>
</head>
<body>
  <svg class="frame" width="1200" height="885" viewBox="0 0 1200 885" aria-hidden="true">
    <path d="M75 0 H1102 Q1123 0 1123 21 V875 H75 Z" fill="var(--slate)"/>
    <path d="M248 226 H1113 V590 C1110 720 1020 830 885 875 H86 V520 C100 380 170 270 248 226 Z" fill="var(--white)"/>
  </svg>

  <header class="site-header">
    <div class="banner">
      <div class="banner-photo" role="img" aria-label="Photo of a conference table surrounded by office chairs"></div>
    </div>
    <div class="brand">Harbourline<br>Mediation</div>
    <nav class="main-nav">
      <a class="nav-home" href="#">Home</a>
      <a class="nav-about" href="#">About Us</a>
      <a class="nav-mediation" href="#">About Mediation</a>
      <a class="nav-scheduling" href="#">Scheduling</a>
      <a class="nav-contact" href="#">Contact Us</a>
    </nav>
  </header>
  <div class="header-rule"></div>

  <main class="content">
    <h2>This text is used just to show space recommended for Text<br>Welcome to Family Mediation</h2>
    <p style="margin-top:12px">Family Mediation&nbsp; is an interdisciplinary association of professionals, working together,<br>creating a better way to provide for co-operative conflict resolution relating to families.</p>
    <p>We help families succeed by providing referrals to Consumers and information to Family<br>Mediators and other like-minded organizations across Canada. Family Mediation in times of<br>conflict can easy, time efficient, inexpensive, dramatically reduce the human and financial<br>cost of conflict resolution. Contact us today for more information.</p>
    <div class="gap"></div>
    <h2>Our Vision:</h2>
    <p>Excellence in Family Mediation.</p>
    <h2>Our Mission:</h2>
    <p>Family Mediation families, workplaces and communities.organization dedicated to the promotion<br>of mediation nd other forms of conflict resolution for individuals,</p>
    <div style="height:12px"></div>
    <h2>Mediation's Greatest Attribute...Simplicity</h2>
    <p>&nbsp;"There's no need for a formal setting, no need for a particular<br>no one under oath. All mediation needs is a valid dispute, people<br>interested in resolving the dispute,<br>and a neutral third party to direct these efforts.<br>Mediation is at its most useful and compelling when<br>it is simple, easy, time efficient, inexpensive, and prompt."<br>format, no discovery, no testimony,</p>
  </main>

  <div class="services svc-one">Arbitraiton &amp; Mediation Services</div>
  <div class="services svc-two">Arbitration &amp; Mediation Services Attorneys</div>
</body>
</html>
```